exclusive Speakeasy Bar Web design in New Jersey USA

We are opening a speakeasy in New Jersey USA soon. we are looking for a web designer to do our web site including the coding. we a looking for a 4 to 5 page web design. the site will be mostly static. home page, contact page, menu page and a link to a 3rd party site (most likely Quob) for reservations. we are looking for this designer to do our menu deign as well. we are looking for a quick turnaround 7-10 days. i am attaching some pictures for the designers to see the concept design and the actual current pictures with our logo as well. professionally taken pictures will be provided later on. our photographer will be taking the pictures in the next week.

Industry/Entity Type

Restaurant, Bar, Speakeasy

Coding

Coded - Design and coding required

Number of Pages Required

4 page

Requirements
Must have
• home page, contact page, menu page and a link to quob.com for reservations
Nice to have
• some videos

```html
<!DOCTYPE html>
<html lang="en">
<head>
<meta charset="utf-8">
<title>217 Parlor — Speakeasy</title>
<link href="https://fonts.googleapis.com/css2?family=Cinzel:wght@400;500&family=Montserrat:wght@400;500;600;700&family=Lora:wght@400;700&display=swap" rel="stylesheet">
<style>
:root{
  --gold:#c9a05a;
  --gold-dark:#b08640;
  --brown:#6c5127;
  --ink:#2b2b2b;
  --body:#444;
  --grey-band:#f5f5f5;
  --white:#fff;
}
*{box-sizing:border-box;margin:0;padding:0}
html,body{width:1200px;height:4225px;overflow:hidden;background:var(--white)}
body{position:relative;font-family:'Montserrat',sans-serif;color:var(--body)}
.abs{position:absolute}
.serif{font-family:'Lora',serif}
.display{font-family:'Cinzel',serif;color:var(--ink);font-weight:400}
.center{text-align:center;left:0;width:1200px}
.eyebrow{font-family:'Cinzel',serif;color:var(--gold);font-size:19px}
.rule{position:absolute;height:2px;width:60px;background:var(--gold)}
.photo{position:absolute}
.btn{position:absolute;border:2px solid var(--gold);font-family:'Cinzel',serif;color:var(--ink);font-size:16px;display:flex;align-items:center;justify-content:center;background:transparent}
.btn::after{content:"";position:absolute;right:-6px;bottom:-6px;width:9px;height:9px;border:1px solid var(--gold);background:var(--white)}
.icon-box{position:absolute;border:1px solid var(--gold);display:flex;align-items:center;justify-content:center}
.round-arrow{position:absolute;width:32px;height:32px;border:1px solid #bbb;border-radius:50%;display:flex;align-items:center;justify-content:center}
.topbar-text{font-family:'Lora',serif;font-size:14px;color:#555;white-space:nowrap}
.nav a{position:absolute;font-family:'Lora',serif;font-size:14px;color:#555;text-decoration:none}
.nav a.active{color:var(--gold);font-weight:700}
.brand-mark{position:absolute;left:554px;top:11px;width:94px;height:120px;background:var(--white);border:2px solid var(--gold);display:flex;flex-direction:column;align-items:center;justify-content:center;z-index:3}
.brand-mark .name{font-family:'Lora',serif;font-size:28px;color:var(--ink);line-height:1}
.brand-mark .sub{font-family:'Lora',serif;font-size:14px;color:var(--ink);margin-top:8px;letter-spacing:1px}
.card{position:absolute;top:775px;width:278px;height:331px;border:2px solid #e9d6b2;background:var(--white)}
.card .photo{left:0;top:0;width:274px;height:241px}
.card h3{position:absolute;top:270px;left:0;width:100%;text-align:center;font-family:'Cinzel',serif;font-weight:400;font-size:18px;color:var(--ink);letter-spacing:.5px}
.card .dot{position:absolute;left:122px;top:313px;width:26px;height:26px;border-radius:50%;background:var(--gold-dark);display:flex;align-items:center;justify-content:center}
.band{position:absolute;left:0;width:1200px}
.para{font-size:12.5px;line-height:22px;color:var(--body)}
.footer-h{font-family:'Montserrat',sans-serif;font-size:17px;color:var(--white);font-weight:500}
.foot-link{position:absolute;left:161px;font-family:'Lora',serif;font-size:13px;color:var(--white)}
.foot-link span{color:var(--gold);margin-right:10px}
.foot-small{font-family:'Lora',serif;font-size:13px;color:var(--white);line-height:18px;white-space:nowrap}
.foot-label{font-family:'Montserrat',sans-serif;font-size:12px;font-weight:600;color:var(--white)}
</style>
</head>
<body>

<header>
  <div class="icon-box" style="left:162px;top:7px;width:28px;height:28px">
    <svg width="14" height="14" viewBox="0 0 24 24"><path d="M6.6 10.8a15 15 0 006.6 6.6l2.2-2.2c.3-.3.7-.4 1-.2 1.1.4 2.3.6 3.6.6.6 0 1 .4 1 1V20c0 .6-.4 1-1 1A17 17 0 013 4c0-.6.4-1 1-1h3.5c.6 0 1 .4 1 1 0 1.3.2 2.5.6 3.6.1.3 0 .7-.2 1z" fill="#c9a05a"/></svg>
  </div>
  <div class="abs topbar-text" style="left:196px;top:12px">+1 555-318-0217</div>
  <div class="abs" style="left:340px;top:10px;width:1px;height:22px;background:#ddd"></div>
  <div class="icon-box" style="left:354px;top:7px;width:28px;height:28px">
    <svg width="14" height="12" viewBox="0 0 24 18"><rect x="1" y="1" width="22" height="16" fill="#c9a05a"/><path d="M1 1l11 9 11-9" stroke="#fff" stroke-width="2" fill="none"/></svg>
  </div>
  <div class="abs topbar-text" style="left:388px;top:12px;font-size:13px">hello@217parlor.com</div>

  <div class="abs serif" style="left:692px;top:7px;width:124px;height:29px;border:2px solid var(--gold);color:var(--gold);font-size:13px;display:flex;align-items:center;justify-content:center">Book Your Event</div>
  <div class="icon-box" style="left:833px;top:7px;width:28px;height:28px"><span style="width:10px;height:10px;background:var(--gold);display:block"></span></div>
  <div class="abs topbar-text" style="left:870px;top:12px;font-size:12px;text-decoration:underline;color:#333">Socialbook</div>
  <div class="icon-box" style="left:943px;top:7px;width:28px;height:28px"><span style="width:10px;height:10px;border-radius:50%;background:var(--gold);display:block"></span></div>
  <div class="abs topbar-text" style="left:982px;top:12px;font-size:12px;text-decoration:underline;color:#333">Snapgram</div>

  <div class="abs" style="left:162px;top:49px;width:876px;height:1px;background:#e5e5e5"></div>
  <nav class="nav">
    <a class="active" href="#" style="left:362px;top:58px">Home</a>
    <div class="abs" style="left:370px;top:80px;width:22px;height:1px;background:var(--gold)"></div>
    <a href="#" style="left:428px;top:58px">Features</a>
    <a href="#" style="left:721px;top:58px">Menu</a>
    <a href="#" style="left:787px;top:58px">Contact Us</a>
  </nav>
  <div class="brand-mark"><div class="name">217</div><div class="sub">PARLOR</div></div>
</header>

<section class="band" style="top:90px;height:480px">
  <div class="photo" role="img" aria-label="Bartender pouring a cocktail in front of a lit back bar" style="left:0;top:0;width:1200px;height:480px;background:radial-gradient(ellipse at 55% 35%,#6b4a30 0%,#2d2118 45%,#0f0c0a 100%)"></div>
  <div class="abs" style="left:0;top:0;width:1200px;height:480px;background:rgba(0,0,0,.3)"></div>
  <svg class="abs" style="left:60px;top:308px" width="30" height="60" viewBox="0 0 30 60"><path d="M28 2L2 30l26 28" stroke="#fff" stroke-width="2" fill="none"/></svg>
  <svg class="abs" style="left:1110px;top:308px" width="30" height="60" viewBox="0 0 30 60"><path d="M2 2l26 28L2 58" stroke="#c9a05a" stroke-width="2" fill="none"/></svg>
  <div class="abs center" style="top:222px;font-family:'Montserrat',sans-serif;font-weight:600;font-size:36px;color:var(--white)">Curate Custom <span style="color:var(--gold)">Eating Encounters</span></div>
  <div class="abs center serif" style="top:280px;font-size:14px;line-height:25px;color:var(--white)">Lorem ipsum dolor sit amet, consectetuer adipiscing elit, sed diam nonummy nibh<br>euismod tincidunt ut laoreet dolore magna aliquam erat volutpat.</div>
  <div class="abs serif" style="left:528px;top:353px;width:142px;height:32px;border:2px solid var(--gold);color:var(--gold);font-size:14px;display:flex;align-items:center;justify-content:center">Book Your Event</div>
  <svg class="abs" style="left:550px;top:430px" width="100" height="52" viewBox="0 0 100 52"><path d="M0 50L50 4l50 46z" fill="#c9a05a"/><path d="M20 50L50 22l30 28" stroke="#fff" stroke-width="1.5" fill="none"/><path d="M50 28v14M44 37l6 6 6-6" stroke="#fff" stroke-width="1.6" fill="none"/></svg>
</section>
<div class="abs" style="left:0;top:570px;width:1200px;height:3px;background:var(--gold)"></div>
<div class="abs" style="left:0;top:576px;width:1200px;height:1px;background:var(--gold)"></div>

<section>
  <div class="abs center eyebrow" style="top:652px">Lorem Ipsum</div>
  <h2 class="abs center display" style="top:680px;font-size:40px">Lorem Ipsum Dolor Sit Amet</h2>
  <div class="rule" style="left:570px;top:732px"></div>

  <article class="card" style="left:161px">
    <div class="photo" role="img" aria-label="Cocktail on a wooden tray" style="background:linear-gradient(135deg,#3a2410,#a7702a 55%,#2a1a0c)"></div>
    <h3>Lorem ipsum dolor</h3>
    <div class="dot"><svg width="8" height="10" viewBox="0 0 8 10"><path d="M2 1l4 4-4 4" stroke="#222" stroke-width="1.6" fill="none"/></svg></div>
  </article>
  <article class="card" style="left:461px">
    <div class="photo" role="img" aria-label="Wooden back bar shelves lined with bottles" style="background:linear-gradient(135deg,#4a3a2c,#7a5a3e 50%,#2a2420)"></div>
    <h3>Consetur adipi scing</h3>
    <div class="dot"><svg width="8" height="10" viewBox="0 0 8 10"><path d="M2 1l4 4-4 4" stroke="#222" stroke-width="1.6" fill="none"/></svg></div>
  </article>
  <article class="card" style="left:761px">
    <div class="photo" role="img" aria-label="Row of spirit bottles on a bar counter" style="background:linear-gradient(135deg,#2a3040,#5a6070 50%,#3a2a22)"></div>
    <h3>Exceptr sint occaecat</h3>
    <div class="dot"><svg width="8" height="10" viewBox="0 0 8 10"><path d="M2 1l4 4-4 4" stroke="#222" stroke-width="1.6" fill="none"/></svg></div>
  </article>

  <div class="btn" style="left:526px;top:1156px;width:144px;height:45px">Contact Us</div>
</section>

<section class="band" style="top:1292px;height:518px;background:var(--grey-band)">
  <div class="abs eyebrow" style="left:165px;top:100px">About Us</div>
  <h2 class="abs display" style="left:158px;top:126px;font-size:44px">217 Parlor</h2>
  <div class="rule" style="left:161px;top:184px"></div>
  <p class="abs para" style="left:164px;top:194px;width:450px">Lorem ipsum dolor sit amet, consectetur adipiscing elit, sed do lorem e eiusmod tempor incididunt ut labore et dolore magna Ut enim ad minim veniam, quis nostrud exercitation ullamco laboris nisi ut aliquip ex ea commodo consequat.</p>
  <p class="abs para" style="left:164px;top:286px;width:450px">Ut enim ad minim veniam, quis nostrud exercitation ullamco laboris nisi ut aliquip ex ea commodo consequat. Duis aute irure dolor in lorem is a reprehenderit in voluptate velit esse cillum dolore</p>
  <div class="btn" style="left:161px;top:380px;width:144px;height:44px">Read More</div>
  <div class="btn" style="left:331px;top:380px;width:144px;height:44px">View Menu</div>
  <div class="abs" style="left:662px;top:105px;width:366px;height:322px;border:1px solid var(--gold)"></div>
  <div class="photo" role="img" aria-label="Lounge interior with curved bar and amber armchairs" style="left:679px;top:90px;width:360px;height:323px;background:linear-gradient(135deg,#2b3438,#4a5458 40%,#9a6a38 75%,#2a2e30)"></div>
  <div class="abs" style="left:1023px;top:429px;width:9px;height:9px;border:1px solid var(--gold);background:var(--grey-band)"></div>
</section>

<section>
  <div class="abs center" style="top:1898px;font-family:'Montserrat',sans-serif;font-size:16px;color:var(--gold);letter-spacing:1px">TESTIMONIALS</div>
  <h2 class="abs center display" style="top:1925px;font-size:37px">Customer Reviews</h2>
  <div class="rule" style="left:570px;top:1975px"></div>
  <svg class="abs" style="left:566px;top:1996px" width="68" height="66" viewBox="0 0 68 66">
    <path d="M14 10A30 30 0 0 0 22 60" stroke="#c9a05a" stroke-width="3" fill="none"/>
    <circle cx="36" cy="33" r="29" fill="#c9a05a"/>
    <circle cx="28" cy="38" r="6" fill="#fff"/><path d="M22 38c0-8 4-13 10-15" stroke="#fff" stroke-width="4" fill="none"/>
    <circle cx="45" cy="38" r="6" fill="#fff"/><path d="M39 38c0-8 4-13 10-15" stroke="#fff" stroke-width="4" fill="none"/>
  </svg>
  <div class="abs center" style="top:2078px;color:var(--gold);font-size:14px;letter-spacing:2px">★★★★★</div>
  <p class="abs center" style="top:2110px;font-size:12.5px;line-height:22px;color:var(--body)">Lorem ipsum dolor sit amet, consectetur adipiscing elit, sed do eiusmod tempor<br>incididunt ut labore Lorem ipsum dolor sit amet, consectetur</p>
  <div class="abs center display" style="top:2164px;font-size:17px">John</div>
  <div class="round-arrow" style="left:271px;top:2117px"><svg width="8" height="10" viewBox="0 0 8 10"><path d="M6 1L2 5l4 4" stroke="#aaa" stroke-width="1.2" fill="none"/></svg></div>
  <div class="round-arrow" style="left:897px;top:2117px"><svg width="8" height="10" viewBox="0 0 8 10"><path d="M2 1l4 4-4 4" stroke="#aaa" stroke-width="1.2" fill="none"/></svg></div>
</section>

<section class="band" style="top:2277px;height:596px;background:var(--grey-band)">
  <div class="abs center" style="top:90px;font-family:'Montserrat',sans-serif;font-size:16px;color:var(--gold);letter-spacing:1px">GALLERY</div>
  <h2 class="abs center display" style="top:117px;font-size:40px">A Passion for Service</h2>
  <div class="rule" style="left:570px;top:168px"></div>
  <div class="photo" role="img" aria-label="Back bar shelves of bottles above glassware" style="left:161px;top:193px;width:429px;height:313px;background:linear-gradient(135deg,#3a2c22,#8a6a4c 50%,#2a2a2c)"></div>
  <div class="photo" role="img" aria-label="Bar room with teal counter" style="left:602px;top:193px;width:213px;height:149px;background:linear-gradient(135deg,#2a2c30,#4a5a58 55%,#7a5a3a)"></div>
  <div class="photo" role="img" aria-label="Amber armchairs in the lounge" style="left:828px;top:193px;width:211px;height:149px;background:linear-gradient(135deg,#2c3034,#b0782e 60%,#3a3430)"></div>
  <div class="photo" role="img" aria-label="Whisky bottle and glass" style="left:602px;top:357px;width:213px;height:149px;background:linear-gradient(135deg,#3a1a08,#c06a1c 50%,#5a2a0c)"></div>
  <div class="photo" role="img" aria-label="Lounge seating facing the bar" style="left:828px;top:357px;width:211px;height:149px;background:linear-gradient(135deg,#2a3034,#3a5a5c 45%,#b07830)"></div>
  <div class="round-arrow" style="left:94px;top:334px"><svg width="8" height="10" viewBox="0 0 8 10"><path d="M6 1L2 5l4 4" stroke="#aaa" stroke-width="1.2" fill="none"/></svg></div>
  <div class="round-arrow" style="left:1072px;top:334px"><svg width="8" height="10" viewBox="0 0 8 10"><path d="M2 1l4 4-4 4" stroke="#aaa" stroke-width="1.2" fill="none"/></svg></div>
</section>

<section class="band" style="top:2873px;height:449px">
  <div class="photo" role="img" aria-label="Video still of a bartender serving a guest at the bar" style="left:0;top:0;width:1200px;height:449px;background:linear-gradient(90deg,#1e1a16,#4a3a2c 40%,#3a2c22 65%,#1c2a3a)"></div>
  <svg class="abs" style="left:571px;top:196px" width="58" height="58" viewBox="0 0 58 58"><circle cx="29" cy="29" r="26" stroke="#fff" stroke-width="3.5" fill="none"/><path d="M23 17l17 12-17 12z" fill="#fff"/></svg>
</section>

<section>
  <div class="abs" style="left:172px;top:3430px;width:366px;height:323px;border:1px solid var(--gold)"></div>
  <div class="photo" role="img" aria-label="Bartender mixing drinks for two guests" style="left:161px;top:3414px;width:360px;height:323px;background:linear-gradient(135deg,#2a2018,#6a4a2a 45%,#1e2a44)"></div>
  <div class="abs" style="left:167px;top:3750px;width:9px;height:9px;border:1px solid var(--gold);background:#fff"></div>
  <p class="abs display" style="left:583px;top:3462px;width:480px;font-size:28px;line-height:37px">Lorem ipsum dolor sit amet conse ctetur adipiscing elit sed do lorem etur eiusmod tempor incididunt utconse Excepteur sint occaeca.</p>
  <div class="btn" style="left:583px;top:3665px;width:143px;height:41px">Contact Us</div>
</section>

<footer class="band" style="top:3824px;height:401px;background:var(--brown)">
  <div class="abs footer-h" style="left:161px;top:60px">Quick Links</div>
  <div class="foot-link" style="top:105px;color:var(--gold)"><span>»</span>Home</div>
  <div class="foot-link" style="top:136px"><span>»</span>Features</div>
  <div class="foot-link" style="top:166px"><span>»</span>Menu</div>
  <div class="foot-link" style="top:195px"><span>»</span>Contact Us</div>

  <div class="abs footer-h" style="left:356px;top:60px">Contact Details</div>
  <div class="icon-box" style="left:356px;top:108px;width:36px;height:36px"><svg width="14" height="18" viewBox="0 0 14 18"><path d="M7 1a6 6 0 00-6 6c0 4.5 6 10 6 10s6-5.5 6-10a6 6 0 00-6-6z" fill="#c9a05a"/><circle cx="7" cy="7" r="2" fill="#6c5127"/></svg></div>
  <div class="abs foot-label" style="left:408px;top:108px">PARLOR</div>
  <div class="abs foot-small" style="left:408px;top:133px">48 Cellar Lane, Suite 2<br>Harbor Town, NJ 07999</div>
  <div class="icon-box" style="left:356px;top:190px;width:36px;height:36px"><svg width="14" height="14" viewBox="0 0 24 24"><path d="M6.6 10.8a15 15 0 006.6 6.6l2.2-2.2c.3-.3.7-.4 1-.2 1.1.4 2.3.6 3.6.6.6 0 1 .4 1 1V20c0 .6-.4 1-1 1A17 17 0 013 4c0-.6.4-1 1-1h3.5c.6 0 1 .4 1 1 0 1.3.2 2.5.6 3.6.1.3 0 .7-.2 1z" fill="#c9a05a"/></svg></div>
  <div class="abs foot-label" style="left:408px;top:190px">Call Us</div>
  <div class="abs foot-small" style="left:408px;top:208px">555 210 4477</div>
  <div class="icon-box" style="left:356px;top:252px;width:36px;height:36px"><svg width="14" height="11" viewBox="0 0 24 18"><rect x="1" y="1" width="22" height="16" fill="#c9a05a"/><path d="M1 1l11 9 11-9" stroke="#6c5127" stroke-width="2" fill="none"/></svg></div>
  <div class="abs foot-label" style="left:408px;top:254px">Mail Us</div>
  <div class="abs foot-small" style="left:408px;top:272px">hello@217parlor.com</div>

  <div class="abs" style="left:770px;top:64px;width:105px;height:136px;border:2px solid var(--gold);display:flex;flex-direction:column;align-items:center;justify-content:center">
    <div style="font-family:'Lora',serif;font-size:30px;color:var(--white);line-height:1">217</div>
    <div style="font-family:'Lora',serif;font-size:15px;color:var(--white);margin-top:8px;letter-spacing:1px">PARLOR</div>
  </div>
  <div class="abs" style="left:620px;top:236px;width:420px;height:1px;background:rgba(255,255,255,.08)"></div>
  <div class="icon-box" style="left:779px;top:265px;width:36px;height:36px"><span style="width:11px;height:11px;background:var(--gold);display:block"></span></div>
  <div class="icon-box" style="left:829px;top:265px;width:36px;height:36px"><span style="width:11px;height:11px;border-radius:50%;background:var(--gold);display:block"></span></div>
</footer>
<div class="abs center serif" style="top:4176px;height:49px;background:var(--gold);color:var(--white);font-size:12px;display:flex;align-items:center;justify-content:center">Copyright © 2025 Parlor . <b>&nbsp;All Rights Reserved.</b></div>

</body>
</html>
```